Events By Halvane

Weddings, Corporate, Special Events
Memorable Catering, Personalized Menus, Custom Layout & Designs
Professional Staff, Excellent Service
Our Mission is Turning YOUR Vision into a Reality

Odette Halvane, Principal Planner
ph. 202 418-7352 - fax 301-847-2951
Email - eventsbyhalvane@mailtrove.com
Web - www.cateringbyhalvane.com
cateringbyhalvane@Instagram

Target Market(s)

All Brides, Corprate Business, Special Events

Industry/Entity Type

Hospitality

Contact Information for Business Card

clean but affective

Font styles to use
Serif
Sans Serif
Script

Colors

Designer to choose colors to be used in the design.

Requirements
Must have
• logo with tagline using colors that will enhance what
• some pictures of nice table scape, hors d'oevures, upscale foods......
Nice to have
• Event: Something that happens or is regarded as happening, an occurrence especially one of some importance.
Should not have
• Use Logo on both sides

```html
<!DOCTYPE html>
<html lang="en">
<head>
<meta charset="utf-8">
<title>Events By Halvane – Business Card</title>
<link href="https://fonts.googleapis.com/css2?family=Cinzel:wght@400;600&family=Poppins:ital,wght@0,400;0,500;0,600;1,400&display=swap" rel="stylesheet">
<style>
  :root {
    --stage: #2b2d30;
    --teal: #1aa6b0;
    --teal-dark: #11808a;
    --ink: #1c1c1c;
    --muted: #5a5a5a;
    --card-black: #1a1819;
    --silver: #9a9a9a;
    --paper: #ffffff;
  }
  * { box-sizing: border-box; margin: 0; padding: 0; }
  html, body { width: 1200px; height: 900px; overflow: hidden; }
  body {
    background: var(--stage);
    font-family: "Poppins", sans-serif;
    position: relative;
  }
  .card {
    position: absolute;
    top: 302px;
    width: 520px;
    height: 297px;
    border-radius: 22px;
    overflow: hidden;
    box-shadow: 0 14px 30px rgba(0,0,0,.45);
  }

  /* Front: contact side */
  .card--front { left: 50px; background: var(--paper); }
  .front__photo {
    position: absolute; top: 0; right: 0; width: 340px; height: 100%;
    background:
      radial-gradient(circle at 70% 70%, #e9c98c 0 14%, transparent 30%),
      radial-gradient(circle at 40% 80%, #9a6a4a 0 10%, transparent 26%),
      radial-gradient(circle at 75% 25%, #c98a6a 0 12%, transparent 28%),
      linear-gradient(135deg, #e2c9a3, #cfa77a 55%, #b98a5e);
  }
  .front__fade {
    position: absolute; top: 0; right: 0; width: 340px; height: 100%;
    background: linear-gradient(90deg, var(--paper) 0%, rgba(255,255,255,.85) 30%, rgba(255,255,255,0) 75%);
  }
  .front__edge { position: absolute; right: 0; top: 0; width: 12px; height: 100%; background: var(--teal); }
  .front__content { position: absolute; left: 28px; top: 26px; }
  .person__name {
    font-family: "Cinzel", serif; font-size: 25px; font-weight: 400; color: var(--ink); letter-spacing: .5px;
  }
  .person__name span { color: var(--teal); }
  .person__title { font-size: 13px; color: var(--muted); margin-top: 2px; }
  .person__rule { width: 12px; height: 3px; background: var(--ink); margin: 18px 0 20px; }
  .contact-list { list-style: none; }
  .contact-list li {
    display: flex; align-items: center; gap: 10px;
    font-size: 14px; color: var(--ink); line-height: 1; margin-bottom: 11px;
  }
  .contact-list svg { width: 14px; height: 14px; flex: none; }
  .hl { color: var(--teal); }
  .social-pill {
    position: absolute; right: 28px; bottom: 24px;
    display: flex; align-items: center; gap: 10px;
    background: #111; color: #fff; border-radius: 22px;
    padding: 6px 18px 6px 6px; font-weight: 600; font-size: 16px;
  }
  .social-pill i { width: 30px; height: 30px; border-radius: 50%; background: #fff; display: block; }

  /* Back: brand side */
  .card--back {
    left: 630px;
    background:
      repeating-linear-gradient(90deg, rgba(255,255,255,.025) 0 2px, transparent 2px 6px),
      var(--card-black);
  }
  .back__edge { position: absolute; left: 0; top: 0; width: 14px; height: 100%; background: var(--teal); }
  .back__band {
    position: absolute; left: 0; right: 0; bottom: 40px; height: 28px;
    background: var(--teal);
    display: flex; align-items: center; justify-content: center;
    font-style: italic; font-size: 13px; color: var(--card-black);
  }
  .brand { position: absolute; left: 0; right: 0; top: 34px; text-align: center; }
  .brand__mark {
    width: 82px; height: 82px; border-radius: 50%; border: 4px solid var(--silver);
    margin: 0 auto 14px;
  }
  .brand__name {
    font-family: "Cinzel", serif; font-weight: 600; font-size: 34px; color: var(--teal); letter-spacing: 1px;
  }
  .brand__tagline {
    font-family: "Cinzel", serif; font-size: 13px; color: #d8d8d8; letter-spacing: 1px; margin-top: 4px;
  }
</style>
</head>
<body>

<section class="card card--front">
  <div class="front__photo" role="img" aria-label="Photo of an upscale brunch table with plated fruit, pastries, omelette and juice"></div>
  <div class="front__fade"></div>
  <div class="front__edge"></div>

  <div class="front__content">
    <h1 class="person__name">Odette <span>Halvane</span></h1>
    <p class="person__title">Principal Planner</p>
    <div class="person__rule"></div>
    <ul class="contact-list">
      <li>
        <svg viewBox="0 0 16 16"><path fill="var(--teal)" d="M3 1h3l1.5 4-2 1.3a9 9 0 0 0 4.2 4.2L11 8.5l4 1.5v3a2 2 0 0 1-2 2A12 12 0 0 1 1 3a2 2 0 0 1 2-2z"/></svg>
        202 418-7352
      </li>
      <li>
        <svg viewBox="0 0 16 16"><rect x="4" y="1" width="8" height="5" fill="none" stroke="var(--teal)" stroke-width="1.6"/><rect x="1" y="6" width="14" height="6" rx="1" fill="var(--teal)"/><rect x="4" y="10" width="8" height="5" fill="#fff" stroke="var(--teal)" stroke-width="1.6"/></svg>
        301-847-2951
      </li>
      <li>
        <svg viewBox="0 0 16 16"><rect x="1" y="3" width="14" height="10" rx="1" fill="var(--teal)"/><path d="M1.5 4l6.5 5 6.5-5" fill="none" stroke="#fff" stroke-width="1.3"/></svg>
        eventsbyhalvane@mailtrove.com
      </li>
      <li>
        <svg viewBox="0 0 16 16"><circle cx="8" cy="8" r="6.5" fill="none" stroke="var(--teal)" stroke-width="1.6"/><ellipse cx="8" cy="8" rx="2.8" ry="6.5" fill="none" stroke="var(--teal)" stroke-width="1.3"/><path d="M1.5 8h13" stroke="var(--teal)" stroke-width="1.3"/></svg>
        <span>www.<span class="hl">catering</span>by<span class="hl">halvane</span>.com</span>
      </li>
    </ul>
  </div>

  <div class="social-pill"><i></i>CateringByHalvane</div>
</section>

<section class="card card--back">
  <div class="back__edge"></div>
  <div class="brand">
    <div class="brand__mark"></div>
    <h2 class="brand__name">Events By Halvane</h2>
    <p class="brand__tagline">Events Designed with You in Mind</p>
  </div>
  <div class="back__band">Our Mission is Turning YOUR Vision into a Reality</div>
</section>

</body>
</html>
```